Pharmacy ad

need 2 pharmacy ads for the phone book. one for Birchfield Pharmacy and one for Corvane Rx Pharmacy. Dimensions for ad is 4.75in x 4.667 in. please see attached examples of ad uploaded as well logos of each pharmacy

```html
<!DOCTYPE html>
<html lang="en">
<head>
<meta charset="utf-8">
<title>Corvane Rx Pharmacy – Directory Ad</title>
<link rel="stylesheet" href="https://fonts.googleapis.com/css2?family=Montserrat:wght@500;600;700;800;900&family=League+Gothic&family=Open+Sans:ital,wght@1,500&display=swap">
<style>
  :root{
    --blue:#3b52a4;
    --blue-dark:#2f4596;
    --green:#6fbe44;
    --white:#ffffff;
    --photo-a:#e9eef1;
    --photo-b:#c9d6dc;
  }
  *{box-sizing:border-box;margin:0;padding:0}
  html,body{width:1200px;height:1200px;overflow:hidden;background:var(--white)}
  .ad{position:relative;width:1200px;height:1200px;background:var(--white);font-family:"Montserrat",sans-serif;color:var(--blue)}
  .abs{position:absolute}

  .brand{left:70px;top:80px;display:flex;align-items:center;gap:28px}
  .brand-dot{width:150px;height:150px;border-radius:50%;background:var(--green)}
  .brand-name{font-weight:700;color:var(--blue);line-height:1.02}
  .brand-name .big{display:block;font-size:80px;letter-spacing:-1px}
  .brand-name .small{display:block;font-size:46px;letter-spacing:1px;margin-top:6px}

  .hours{right:64px;top:104px;text-align:right;font-weight:600;font-size:27px;line-height:1.05}
  .hours h3{font-weight:800;font-size:26px;margin-bottom:12px}
  .hours p + p{margin-top:12px}

  .tagline{right:62px;top:280px;font-family:"Open Sans",sans-serif;font-style:italic;font-weight:500;font-size:43px;color:var(--green)}

  .photo{left:0;top:289px;width:632px;height:454px;background:linear-gradient(120deg,var(--photo-a),var(--photo-b) 55%,#e6ecef)}
  .services-panel{left:0;top:339px;width:1200px;height:404px}
  .services{left:650px;top:372px;list-style:none;font-weight:600;font-size:30px;color:var(--white);line-height:1.18}
  .services li{position:relative;padding-left:40px;margin-bottom:10px}
  .services li svg{position:absolute;left:0;top:6px}

  .discount-band{left:0;top:743px;width:1200px;height:202px;background:var(--green)}
  .card{top:762px;height:166px;background:var(--white);border-radius:16px 4px 16px 4px;text-align:center;color:var(--blue);overflow:hidden}
  .card .pct{font-weight:900;font-size:118px;line-height:100px;letter-spacing:-6px;margin-top:16px}
  .card .label{font-family:"League Gothic",sans-serif;font-weight:400;font-size:44px;line-height:40px;margin-top:4px;white-space:nowrap}
  .card-senior{left:65px;width:367px}
  .card-student{left:444px;width:310px;text-align:left;padding-left:12px}
  .card-hospital{left:767px;width:367px}
  .card .note{position:absolute;right:10px;top:14px;writing-mode:vertical-rl;font-size:13px;font-weight:500}

  .orders-bar{left:0;top:946px;width:785px;height:61px}
  .orders-text{left:64px;top:955px;font-weight:700;font-size:33px;color:var(--white);letter-spacing:.3px}

  .address{left:64px;top:1020px;font-weight:600;font-size:24px;line-height:1.25}
  .contact{left:64px;top:1096px;display:flex;align-items:center;gap:10px;font-weight:600;font-size:31px}
  .contact .gap{width:8px}

  .social{left:547px;top:1020px;display:flex;align-items:center;gap:14px}
  .social .sq{width:60px;height:60px;background:var(--blue)}
  .social .txt{font-weight:700;line-height:1}
  .social .txt small{display:block;font-size:25px}
  .social .txt span{display:block;font-size:34px;margin-top:4px}

  .accept{left:850px;top:985px;width:330px;text-align:center}
  .accept h4{font-weight:500;font-size:22px;letter-spacing:9px;margin-bottom:10px}
  .partner{font-weight:800;font-size:32px;color:var(--blue);display:flex;align-items:center;justify-content:center;gap:10px}
  .partner i{display:inline-block;width:24px;height:24px;background:var(--green);border-radius:50%}
  .payments{display:flex;justify-content:center;align-items:center;gap:22px;margin-top:20px}
  .badge{width:44px;height:44px;border-radius:50%;background:var(--green)}
  .pay{font-weight:700;font-size:22px;color:var(--blue)}
</style>
</head>
<body>
<div class="ad">

  <div class="abs brand">
    <span class="brand-dot"></span>
    <div class="brand-name"><span class="big">Corvane Rx</span><span class="small">PHARMACY</span></div>
  </div>

  <div class="abs hours">
    <h3>OPENING HOURS</h3>
    <p>Mon - Sat<br>8am - 7pm</p>
    <p>Sun - 10am-2pm</p>
  </div>

  <div class="abs tagline">Where good health begins</div>

  <div class="abs photo" role="img" aria-label="Photo of a smiling pharmacist in a white coat helping a customer at a pharmacy counter with shelves behind"></div>

  <svg class="abs services-panel" viewBox="0 0 1200 404" aria-hidden="true">
    <polygon points="610,0 1200,0 1200,404 507,404" fill="var(--blue)"/>
  </svg>

  <ul class="abs services">
    <li><svg width="28" height="26" viewBox="0 0 28 26"><path d="M2 14 L10 22 L26 2" fill="none" stroke="var(--green)" stroke-width="5" stroke-linecap="round" stroke-linejoin="round"/></svg>Certified Pharmacists</li>
    <li><svg width="28" height="26" viewBox="0 0 28 26"><path d="M2 14 L10 22 L26 2" fill="none" stroke="var(--green)" stroke-width="5" stroke-linecap="round" stroke-linejoin="round"/></svg>Affordable prices</li>
    <li><svg width="28" height="26" viewBox="0 0 28 26"><path d="M2 14 L10 22 L26 2" fill="none" stroke="var(--green)" stroke-width="5" stroke-linecap="round" stroke-linejoin="round"/></svg>Brand and Generic Medicines</li>
    <li><svg width="28" height="26" viewBox="0 0 28 26"><path d="M2 14 L10 22 L26 2" fill="none" stroke="var(--green)" stroke-width="5" stroke-linecap="round" stroke-linejoin="round"/></svg>Blood Pressure and<br>Glucose checks</li>
    <li><svg width="28" height="26" viewBox="0 0 28 26"><path d="M2 14 L10 22 L26 2" fill="none" stroke="var(--green)" stroke-width="5" stroke-linecap="round" stroke-linejoin="round"/></svg>Personal care and Beauty<br>Products</li>
    <li><svg width="28" height="26" viewBox="0 0 28 26"><path d="M2 14 L10 22 L26 2" fill="none" stroke="var(--green)" stroke-width="5" stroke-linecap="round" stroke-linejoin="round"/></svg>Injectables</li>
  </ul>

  <div class="abs discount-band"></div>
  <div class="abs card card-senior"><div class="pct">10%</div><div class="label">SENIOR CITIZEN DISCOUNT</div></div>
  <div class="abs card card-student"><div class="pct">10%</div><div class="label">STUDENT DISCOUNT</div><span class="note">With valid ID card</span></div>
  <div class="abs card card-hospital"><div class="pct">10%</div><div class="label">HOSPITAL PRESCRIPTIONS</div></div>

  <svg class="abs orders-bar" viewBox="0 0 785 61" aria-hidden="true">
    <polygon points="0,0 785,0 767,61 0,61" fill="var(--blue)"/>
  </svg>
  <div class="abs orders-text">SPECIAL ORDERS | DELIVERY SERVICE</div>

  <div class="abs address">Unit B4, Marlow Court Plaza,<br>Harbour Street, Westhaven</div>

  <div class="abs contact">
    <svg width="32" height="32" viewBox="0 0 32 32" aria-hidden="true"><circle cx="16" cy="16" r="14" fill="none" stroke="var(--green)" stroke-width="2"/><path d="M11 8 l3 0 l1.5 4 l-2 1.5 q1.5 3.5 5 5 l1.5 -2 l4 1.5 l0 3 q-1 2 -3 2 q-10 -1 -12 -12 q0 -2 2 -3z" fill="none" stroke="var(--green)" stroke-width="1.8" stroke-linejoin="round"/></svg>
    <span>1 555 210 4836</span>
    <span class="gap"></span>
    <svg width="32" height="32" viewBox="0 0 32 32" aria-hidden="true"><circle cx="16" cy="16" r="14" fill="none" stroke="var(--green)" stroke-width="2"/><rect x="9" y="11" width="14" height="10" rx="1" fill="none" stroke="var(--green)" stroke-width="1.8"/><path d="M9 11 l7 6 l7 -6" fill="none" stroke="var(--green)" stroke-width="1.8"/></svg>
    <span>corvanerx@mailbox.test</span>
  </div>

  <div class="abs social">
    <span class="sq"></span>
    <div class="txt"><small>Visit us on:</small><span>Linkwall</span></div>
  </div>

  <div class="abs accept">
    <h4>WE ACCEPT</h4>
    <div class="partner"><i></i>Halvern Cover</div>
    <div class="payments">
      <span class="badge"></span>
      <span class="pay">PayCircle</span>
      <span class="pay">Trevo</span>
    </div>
  </div>

</div>
</body>
</html>
```